!! We Need YOU !! Las Vegas !! Pool Cleaning Company looking for a Brochure Design!

We are a pool/spa/water feature cleaning company for commercial properties. We are looking for a professional looking brochure to hand to clients as we speak to them about our business. We would like something that stays away from back yard pool themes like pool toys and diving boards. Our properties are resorts, hotels, casinos, and private estates so we need something to grab their attention!

Our company name is "Premier Basin Custodians"
Our slogan is "Sparkling Results"
Phone is 702-538-1726
email is rkellar@prebasincustodiansllc.example
webpage www.pre-basin-custodiansllc.example
(I know those are long! Sorry!)

We DO NOT need to include all of this in one brochure but here are some ideas for wording:

Swimming pools are a way of life in Las Vegas and PBC loves being a part of that culture. PBC is a company that has a team with 15 years of experience that spans across the Las Vegas Valley working on commercial properties. We understand the complexity of managing commercial pools and bring our resources and experience to provide you with a service that can not be matched.

the PBC advantage:
Since 2002 our team has had the privilege of providing services to resorts, casinos, hotels, and private estates. The tried and true business practices of our team have been tested and refined over the years. These practices have resulted in a set of standards to ensure PBC is a company of distinction. We believe our commitment to safety, integrity, affordability, and professionalism help us deliver the best possible pool cleaning services in Las Vegas.

Safety: PBC understands the specific requirements of the health department and chemical regulations. We work closely with the health department and exceed their requirements to help keep your property safe and compliant. PBC has developed a set of systems and programs that have been proven within the industry to accomplish reliance to safety. Our employees are dedicated to using the most advanced tools, training, and technology available to keep your property clean and safe.
Integrity:
You are secure with PBC. We pride ourselves on providing our customers with the right care for your property through honest and straightforward service. PBC will adhere to quality and honesty. PBC will have an active regard for our standards of conduct. It is our sincere belief that by establishing relationships through responsiveness to the customer's needs and dedication to our customers, that we will become the standard by which all other companies will measure their success.

Affordability: You can be assured that PBC will provide professional services at a reasonable rate. PBC will establish a long-term and beneficial relationship while fixing your costs for the next 1-5 years. We strive to keep our focus on commercial properties which means our focus is on your property. We offer exceptional pricing on cleaning, maintenance, and repair services.
Professionalism:
With any industry, you have a spectrum of professionalism. PBC strives to be at the top of that spectrum by encompassing all of the aforementioned qualities, plus many more. We strive to be the leader in providing quality service through education and certification. PBC employees always show respect for you and your property and are highly knowledgeable, courteous, and efficient. PBC will exceed expectations in the areas of accountability, customer support, and expertise.

We will be proactive rather than reactive to potentially problematic areas with proper advance planning.

When you work with PBC you can trust that our experience in the hospitality industry brings unlimited service, quick response, and a reputation to serve. If you have a commercial pool in the Las Vegas area, you should have our number.
If you are looking for knowledgeable and dependable pool cleaning and maintenance in Las Vegas, look no further than PBC.

Maintenance
▪ Regular Maintenance Services
▪ Weekly Pool/Spa Service
▪ One Time Clean-Ups
▪ DE Filter Cleaning
▪ Drain Pool & Refill
▪ Impellers
▪ Valves
▪ Algae Removal
▪ Back Wash
▪ Water Testing & Balancing
▪ Equipment Inspection
▪ Skimming, Brushing, & Leafing
Emergency service 24 hours per day, 7 days per week

Target Market(s)

High-end Resorts and properties.

Industry/Entity Type

It Company

Font styles to use
Serif
Sans Serif

Requirements
Must have
• Professional look and feel.
• Size/shape will depend on design concept-I do not care if it is traditional fold or something creative.
• Needs to have a front and back complete concept.
Nice to have
• I would like to see some ideas using our font and colors.
• I would like to focus on pictures with no buildings or beaches in them.
Should not have
• No pool toys, diving boards, palm trees, beach, or anything with a "backyard" pool feel.

```html
<!DOCTYPE html>
<html lang="en">
<head>
<meta charset="utf-8">
<title>Premier Basin Custodians – Brochure Inner Spread</title>
<link rel="stylesheet" href="https://fonts.googleapis.com/css2?family=Michroma&family=Sorts+Mill+Goudy&display=swap">
<style>
  :root {
    --paper: #dcedf8;
    --ink: #1e1e1e;
    --heading-blue: #3f82cb;
    --divider: #bcdcf1;
    --band-light: #5ab5e6;
    --band-dark: #4878bd;
  }
  * { box-sizing: border-box; margin: 0; padding: 0; }
  html, body { width: 1200px; height: 900px; overflow: hidden; }
  body { background: var(--paper); }
  .spread {
    position: relative;
    width: 1200px;
    height: 900px;
    background: var(--paper);
    color: var(--ink);
    font-family: "Sorts Mill Goudy", "Goudy Old Style", Georgia, serif;
    font-size: 20.5px;
    overflow: hidden;
  }
  .panel-divider {
    position: absolute;
    left: 598px; top: 0;
    width: 2px; height: 857px;
    background: var(--divider);
  }
  .text-block {
    position: absolute;
    white-space: nowrap;
  }
  .text-block p { line-height: 24.8px; }
  .left-panel { left: 50px; }
  .right-panel { left: 637px; }
  .drop-cap {
    font-size: 64px;
    line-height: 0;
    vertical-align: baseline;
  }
  .tracked { letter-spacing: 1.3px; }
  .brand {
    font-family: "Michroma", "Eurostile", Arial, sans-serif;
    font-size: 14px;
    letter-spacing: 0.3px;
  }
  .section-heading {
    position: absolute;
    font-family: "Michroma", "Eurostile", Arial, sans-serif;
    font-size: 13.5px;
    font-weight: 400;
    letter-spacing: 1.6px;
    color: var(--heading-blue);
    text-transform: uppercase;
    white-space: nowrap;
  }
  .footer-band-light {
    position: absolute; left: 0; top: 857px;
    width: 1200px; height: 21px;
    background: var(--band-light);
  }
  .footer-band-dark {
    position: absolute; left: 0; top: 878px;
    width: 1200px; height: 22px;
    background: var(--band-dark);
  }
</style>
</head>
<body>
<main class="spread">
  <div class="panel-divider"></div>

  <!-- Left panel -->
  <div class="text-block left-panel" style="top:62px">
    <p><span class="drop-cap">S</span>wimming pools are a way of life in Las Vegas<br>
    and <span class="brand">PBC</span> loves being a part of that culture.<br>
    <span class="brand">PBC</span> is a company that has a team with 15<br>
    years of experience that spans across the<br>
    Las Vegas Valley <span class="tracked">working on commercial</span><br>
    <span class="tracked">properties.</span></p>
  </div>

  <div class="text-block left-panel" style="top:219px">
    <p>We understand the complexity of managing<br>
    commercial pools and bring our resources and<br>
    experience to provide you with a service that can<br>
    not be matched.</p>
  </div>

  <h2 class="section-heading" style="left:50px; top:335px">The PBC Advantage:</h2>
  <div class="text-block left-panel" style="top:355px">
    <p>Since 2002 our team has had the privilege of<br>
    providing services to resorts, casinos, hotels, and<br>
    private estates. The tried and true business<br>
    practices of our team have been tested and refined<br>
    over the years. These practices have resulted in a<br>
    set of standards to ensure <span class="brand">PBC</span>&nbsp; is a company of<br>
    distinction. We believe our commitment to safety,<br>
    integrity, affordability, and professionalism help<br>
    us deliver the best possible pool cleaning services<br>
    in Las Vegas.</p>
  </div>

  <h2 class="section-heading" style="left:50px; top:621px">Safety:</h2>
  <div class="text-block left-panel" style="top:640px">
    <p>PBC understands the specific requirements of the<br>
    health department and chemical regulations.</p>
  </div>
  <div class="text-block left-panel" style="top:698px">
    <p>We work closely with the health department and<br>
    exceed their requirements to help keep your<br>
    property safe and compliant. <span class="brand">PBC</span> has developed<br>
    a set of systems and programs that have been<br>
    <span class="tracked">proven within the industry to accomplish</span><br>
    <span class="tracked">reliance to safety.</span></p>
  </div>

  <!-- Right panel -->
  <div class="text-block right-panel" style="top:33px">
    <p>Our employees are dedicated to using the most<br>
    advanced tools, training, and technology<br>
    available to keep your property clean and safe.</p>
  </div>

  <h2 class="section-heading" style="left:637px; top:127px">Integrity:</h2>
  <div class="text-block right-panel" style="top:146px">
    <p>You are secure with <span class="brand">PBC</span>. We pride ourselves on<br>
    providing our customers with the right care for<br>
    your property through honest and straightforward<br>
    service.&nbsp; <span class="brand">PBC</span> will adhere to quality and honesty.<br>
    <span class="brand">PBC</span> will have an active regard for our standards<br>
    of conduct. It is our sincere belief that by<br>
    establishing relationships through responsiveness<br>
    to the customer’s needs and dedication to our<br>
    customers, that we will become the standard by<br>
    which all other companies will measure their<br>
    success.</p>
  </div>

  <h2 class="section-heading" style="left:637px; top:441px">Affordability:</h2>
  <div class="text-block right-panel" style="top:460px">
    <p>You can be assured that <span class="brand">PBC</span> will provide<br>
    professional services at a reasonable rate. <span class="brand">PBC</span><br>
    <span class="tracked">will establish a long-term and beneficial</span><br>
    relationship while fixing your costs for the next<br>
    <span class="tracked">1-5 years. We strive to keep our focus on</span><br>
    commercial properties which means our focus is<br>
    on your property. We offer exceptional pricing on<br>
    cleaning, maintenance, and repair services.<br>
    Professionalism:&nbsp; With any industry, you have a<br>
    spectrum of professionalism. <span class="brand">PBC</span> strives to be<br>
    at the top of that spectrum by encompassing all of<br>
    the aforementioned qualities, plus many more.</p>
  </div>

  <div class="text-block right-panel" style="top:767px">
    <p>We strive to be the leader in providing quality<br>
    service through education and certification. <span class="brand">PBC</span><br>
    employees always show respect for you and your</p>
  </div>

  <div class="footer-band-light"></div>
  <div class="footer-band-dark"></div>
</main>
</body>
</html>
```